sailbrightly Website for children with diabilities

Hi, we are looking for a new website design for our community service "sailbrightly". Sailbrightly gives children who suffer from diseases or disabilities a week off on a Boat to give the children new hope and an unforgettable experience.

The current website is really old and we want to have a new one.
Please feel free to discover our website under http://sailbrightly-example.at/.
We have several company sponsors which are very important to us.

The Website has to be a Bootstrap Design (Version 4.4 or higher) [NOT Wordpress, Joomla, other CMS]

Target Market(s)

no target market. we like to inform our communities about our service.

Industry/Entity Type

community service for children with disabilities

Coding

Number of Pages Required

4 page

Font styles to use
Sans Serif

Colors
0054AA
0677BA
7BADD7
CADEEF
E8F1F8
0094D4
00A9DD
6FCCEA
C7EBF8
E9F6FB

Requirements
Must have
• About, Sponsors, Information about cruises
Nice to have
• Gallery

```html
<!DOCTYPE html>
<html lang="de">
<head>
<meta charset="utf-8">
<title>Verein Sail Brightly</title>
<link href="https://fonts.googleapis.com/css2?family=Poppins:wght@400;500;600;700&family=Roboto:wght@400;500&display=swap" rel="stylesheet">
<style>
:root{
  --navy:#1b2262;
  --blue:#0054aa;
  --mid:#0677ba;
  --sky:#7badd7;
  --pale:#cadeef;
  --mist:#eef4f9;
  --footer:#bdd5ee;
  --text:#2b2b2b;
  --white:#ffffff;
}
*{margin:0;padding:0;box-sizing:border-box}
html,body{width:1200px;height:3358px;overflow:hidden}
body{position:relative;background:var(--white);font-family:'Roboto',sans-serif;color:var(--text)}
.abs{position:absolute}
h1,h2,h3{font-family:'Poppins',sans-serif;color:var(--navy);font-weight:700}
.section-title{font-size:36px;line-height:1.2}
.center{text-align:center}
.body-text{font-size:13.5px;line-height:24px}

/* hero */
.hero{left:0;top:0;width:1200px;height:560px;overflow:hidden}
.hero-photo{position:absolute;inset:0;background:linear-gradient(180deg,#cfe2ef 0%,#5fb3cf 22%,#2c9bbd 40%,#b8c4c8 58%,#d9a0a0 72%,#c86a6a 100%)}
.hero-curve{position:absolute;left:0;bottom:0}
.brand{left:0;width:1200px;top:14px;font-family:'Poppins',sans-serif;font-size:27px;color:#111;text-align:center;font-weight:400}
.brand b{font-weight:600}
.brand-mark{left:550px;top:56px;width:96px;height:96px;border-radius:50%;background:var(--navy)}
.nav{top:20px;font-size:13.5px;color:#111;font-family:'Roboto',sans-serif}
.hero-quote{left:300px;width:600px;top:174px;text-align:center;color:var(--white);font-family:'Poppins',sans-serif;font-weight:600;font-size:27px;line-height:35px;text-shadow:0 1px 3px rgba(0,0,0,.35)}
.hero-cite{left:0;width:1200px;top:294px;text-align:center;color:var(--navy);font-family:'Poppins',sans-serif;font-style:italic;font-size:11.5px}

/* photos */
.photo{border-radius:2px}
.polaroid{position:absolute;background:#fafafa;padding:18px;box-shadow:10px 10px 0 #6c6c6c,0 0 6px rgba(0,0,0,.15)}
.polaroid .pic{width:100%;height:100%}
.tape{position:absolute;width:70px;height:26px;background:rgba(173,210,235,.7)}

/* goals grid */
.goal{position:absolute;display:flex;align-items:center;justify-content:center;text-align:center;color:var(--white);font-family:'Poppins',sans-serif;font-weight:500;font-size:15.5px;line-height:24px;padding:0 20px}

.band{left:0;width:1200px;top:2530px;height:280px;background:var(--mist)}
.thanks{left:0;width:1200px;top:2844px;text-align:center;font-family:'Poppins',sans-serif;color:var(--navy);font-size:17.5px;line-height:26px}
.sponsor{top:2955px;height:80px;display:flex;align-items:center;justify-content:center;font-family:'Poppins',sans-serif;font-weight:700;color:var(--blue);font-size:30px;width:230px}
.dot{top:3078px;width:14px;height:14px;border-radius:50%;border:2px solid var(--mid)}
.dot.on{background:var(--mid)}
.footer{left:0;top:3185px;width:1200px;height:173px;background:var(--footer)}
.footer-name{left:0;width:1200px;top:3212px;text-align:center;font-family:'Poppins',sans-serif;font-size:22px;color:#111}
.footer-name b{font-weight:600}
.footer-mark{left:560px;top:3250px;width:78px;height:78px;border-radius:50%;background:var(--navy)}
.copy{left:0;width:1200px;top:3335px;text-align:center;font-size:11px;color:#222}
</style>
</head>
<body>

<header class="abs hero">
  <div class="hero-photo" role="img" aria-label="Kinderhände mit bunt bemalten Buchstaben vor Meer, Felsen und Segelboot"></div>
  <svg class="hero-curve" width="1200" height="70" viewBox="0 0 1200 70" preserveAspectRatio="none">
    <path d="M0 10 Q600 85 1200 10 L1200 70 L0 70 Z" fill="#ffffff"/>
  </svg>
</header>
<div class="abs brand">Verein <b>Sail Brightly</b></div>
<div class="abs brand-mark"></div>
<nav>
  <span class="abs nav" style="left:948px">Sponsoren</span>
  <span class="abs nav" style="left:1048px">Flotteninfos 2022</span>
</nav>
<p class="abs hero-quote">Wir können die Windrichtung nicht bestimmen, aber wir können die Segel richtig setzen!</p>
<p class="abs hero-cite">Marcus Velleius</p>

<section>
  <h2 class="abs section-title center" style="left:0;width:1200px;top:584px">Wir sind...</h2>
  <p class="abs body-text center" style="left:330px;width:540px;top:644px">...ausgebildete SozialpädagogInnen und erfahrene SkipperInnen, die sich ehrenamtlich im Verein Sail Brightly engagieren und alljährlich für sozial benachteiligte Kinder und Jugendliche, aus dem oberösterreichischen Zentralraum, eine Flotte organisieren und die dafür notwendigen finanziellen Mittel aufstellen.</p>
</section>

<section>
  <h2 class="abs section-title" style="left:111px;top:824px">Wir wollen...</h2>
  <p class="abs body-text" style="left:111px;width:462px;top:884px">...Kindern und Jugendlichen, die es im Leben nicht immer leicht haben, eine unvergessliche Woche in Kroatien ermöglichen. Denn genau dieses gemeinsame Erlebnis vermittelt den Kindern und Jugendlichen neue Lebensfreude und Perspektiven für ihre Zukunft. Durch die Reflexion und auch die Betreuung danach in den einzelnen Einrichtungen, können die Kinder und Jugendlichen noch lange an diesem Erlebnis zehren. Diese Nachhaltigkeit schafft zahlreiche pädagogische Anknüpfungspunkte, die für die Zielerreichung eine wertvolle Grundlage darstellen.</p>
  <div class="abs photo" style="left:636px;top:812px;width:453px;height:314px;background:linear-gradient(160deg,#5aa6d8,#2d7fc0 55%,#1f5d9c)" role="img" aria-label="Jugendliche holen gemeinsam ein Seil an Deck ein"></div>
</section>

<section>
  <h2 class="abs section-title center" style="left:0;width:1200px;top:1220px">Praktische Umsetzung der<br>pädagogischen Überlegungen</h2>
  <p class="abs body-text" style="left:111px;width:455px;top:1374px">Die TeilnehmerInnen werden bewusst zu Tätigkeiten beim Segeln herangezogen. Es gibt Verantwortlichkeiten für verschiedenste Aufgaben im täglichen Zusammenleben. Ein Koch- und Putzplan soll dazu beitragen, Verantwortung gegenüber der Gruppe zu übernehmen. Die Tatsache, ein Segelschiff alleine zu steuern, erfüllt so manchen mit großem Stolz. Wiederkehrende Tätigkeiten am Schiff erfordern die Beteiligung jedes Crewmitglieds.</p>

  <div class="polaroid" style="left:642px;top:1370px;width:255px;height:215px;transform:rotate(-4deg)">
    <div class="pic" style="background:linear-gradient(170deg,#6fb4e2,#2f7fc4 60%,#d9e6ee)" role="img" aria-label="Kinder sitzen auf dem Vorschiff eines Segelboots"></div>
  </div>
  <div class="polaroid" style="left:862px;top:1372px;width:210px;height:205px;transform:rotate(6deg)">
    <div class="pic" style="background:linear-gradient(160deg,#8cc7ea,#3a8fcf 60%,#1d4f86)" role="img" aria-label="Junge am Steuerrad eines Segelboots"></div>
  </div>
  <div class="tape" style="left:770px;top:1350px;transform:rotate(35deg)"></div>
  <div class="tape" style="left:960px;top:1365px;transform:rotate(-75deg)"></div>

  <div class="polaroid" style="left:120px;top:1585px;width:230px;height:210px;transform:rotate(5deg)">
    <div class="pic" style="background:linear-gradient(160deg,#9cc8e8,#e4d6d0 55%,#5a7aa0)" role="img" aria-label="Mädchen hält eine Leine an Bord"></div>
  </div>
  <div class="polaroid" style="left:365px;top:1608px;width:200px;height:215px;transform:rotate(-11deg)">
    <div class="pic" style="background:linear-gradient(160deg,#cfe6f5,#4c9fd8 55%,#d24a2a)" role="img" aria-label="Junge mit Schwimmweste an Deck"></div>
  </div>
  <div class="tape" style="left:200px;top:1585px;transform:rotate(-32deg)"></div>
  <div class="tape" style="left:420px;top:1605px;transform:rotate(-60deg)"></div>

  <p class="abs body-text" style="left:646px;width:445px;top:1640px">So wird allen das Gefühl vermittelt, eine Bedeutung für die Gemeinschaft zu haben und jede/r lernt dabei, diese Verantwortung nach eigener Möglichkeit auch zu tragen. Sail Brightly bietet ein ideales Übungsfeld für soziales Lernen. Die intensive Auseinandersetzung mit anderen und der Gruppe auf engstem Raum, bietet verschiedenste Möglichkeiten, sich im Umgang mit Mitmenschen zu erproben. All diese Erfahrungen können zu einer Aufwertung ihrer selbst führen.</p>
</section>

<section>
  <h2 class="abs section-title" style="left:111px;top:1966px">Projektziele</h2>
  <div class="goal" style="left:111px;top:2050px;width:475px;height:353px;background:linear-gradient(150deg,#8fa8c4,#6c88ac 50%,#50709a)" role="img" aria-label="Lachende Jugendliche am Strand">Stärkung des Selbstwertgefühls<br>und der sozialen Kompetenz</div>
  <div class="goal" style="left:595px;top:2050px;width:242px;height:172px;background:linear-gradient(160deg,#5f7a8e,#6b8a7a)" role="img" aria-label="Kinder spielen gemeinsam im Freien">Verantwortung für sich selbst und andere übernehmen</div>
  <div class="goal" style="left:846px;top:2050px;width:242px;height:172px;background:linear-gradient(160deg,#8f7fa6,#7a8cb0)" role="img" aria-label="Kinder legen die Hände übereinander">Üben von Toleranz</div>
  <div class="goal" style="left:595px;top:2231px;width:242px;height:172px;background:linear-gradient(160deg,#6a6c78,#7f6e72)" role="img" aria-label="Kinder im Gespräch">Erarbeiten gewaltfreier Konfliktlösungsstrategien</div>
  <div class="goal" style="left:846px;top:2231px;width:242px;height:172px;background:linear-gradient(160deg,#6f8aa0,#7f9aae)" role="img" aria-label="Kinder lernen draußen in der Natur">Erlebnisorientiertes Lernen</div>
</section>

<section>
  <div class="abs band"></div>
  <h2 class="abs section-title center" style="left:0;width:1200px;top:2566px">Erreichte Ziele</h2>
  <p class="abs body-text center" style="left:330px;width:540px;top:2627px">Durch das Erlebnis einer gemeinsamen Segelwoche schafft die "Sail Brightly Flotte" ideale Bedingungen, unter denen die Leitziele wie soziale Integration und pädagogische Weiterentwicklung der Kinder auf konkrete, effiziente und professionelle Weise, und mit nachhaltiger Wirkung umgesetzt wurden.</p>
</section>

<section>
  <p class="abs thanks">Wir bedanken uns für Ihr großartiges Engagement<br>und Ihre Unterstützung:</p>
  <div class="abs sponsor" style="left:75px;color:#1e7f86">Hallbrunner</div>
  <div class="abs sponsor" style="left:345px;flex-direction:column;line-height:1.05">Velmora<span style="font-size:19px">www.velmora-example.at</span></div>
  <div class="abs sponsor" style="left:610px;color:#111;font-size:27px">Kreitmayr Bau</div>
  <div class="abs sponsor" style="left:880px;color:#777;font-size:26px">Lindtaler</div>
  <div class="abs dot on" style="left:548px"></div>
  <div class="abs dot" style="left:578px"></div>
  <div class="abs dot" style="left:608px"></div>
  <div class="abs dot" style="left:638px"></div>
</section>

<footer>
  <div class="abs footer"></div>
  <div class="abs footer-name">Verein <b>Sail Brightly</b></div>
  <div class="abs footer-mark"></div>
  <div class="abs copy">© Sailbrightly 2022</div>
</footer>

</body>
</html>
```